Banner Ad for Resume Writers

This ad is for www.kelbrancareers.com.au

The site offers a resume writing service in Australia. Take a look at the site for more info.

Colours to use: Blue, orange, yellow or whatever works.

Image specifications:
Pixel size: 160w X 600h (Skyscraper)
Image format: GIF (25K max)
Must have a border and must not use transparent backgrounds

Text can include:

'Professional Resume Writers'

and

'Is your resume good enough? Ask the Experts!'

The text 'Free resume health check' could be included but the banner should look good even if this text is not included as it may need to be removed.

Target Market(s)

Job seekers

Industry/Entity Type

Health

Nice to have
• It would be good to include an attractive smiling face making eye contact with the viewer.
Should not have
• Should not be too busy. Avoid clutter.

```html
<!DOCTYPE html>
<html lang="en">
<head>
<meta charset="UTF-8">
<title>Professional Resume Writers – Skyscraper Banners</title>
<link rel="stylesheet" href="https://fonts.googleapis.com/css2?family=Rokkitt:wght@400;600;700&family=Oswald:wght@600&display=swap">
<style>
  :root {
    --page: #ffffff;
    --ink: #2b2b2b;
    --white: #ffffff;
    --frame: #1a1a1a;

    --green-top: #4cc42c;
    --green-bottom: #2d8c17;
    --blue-top: #2aa6cc;
    --blue-bottom: #1a6a90;
    --teal-top: #28c6c2;
    --teal-bottom: #17908f;
    --red-top: #cc2a40;
    --red-bottom: #8a1522;
    --red-ink: #5e0e16;

    --skin-deep: #d9a88e;
    --skin-light: #f3dccd;

    --btn-red-top: #f05858;
    --btn-red-bottom: #c40a0a;
    --btn-green-top: #b4e65a;
    --btn-green-bottom: #5aa60e;
    --btn-blue-top: #66bdf2;
    --btn-blue-bottom: #1a6cc4;
  }

  * { box-sizing: border-box; margin: 0; padding: 0; }

  html, body {
    width: 1200px;
    height: 800px;
    overflow: hidden;
    background: var(--page);
  }

  .canvas {
    position: relative;
    width: 1200px;
    height: 800px;
  }

  .banner {
    position: absolute;
    top: 90px;
    width: 162px;
    height: 602px;
    border: 1px solid var(--frame);
    overflow: hidden;
    font-family: "Rokkitt", Georgia, serif;
    color: var(--white);
    --top: var(--green-top);
    --bottom: var(--green-bottom);
  }
  .banner--one   { left: 82px; }
  .banner--two   { left: 293px; --top: var(--blue-top); --bottom: var(--blue-bottom); }
  .banner--three { left: 512px; --top: var(--teal-top); --bottom: var(--teal-bottom); }
  .banner--four  { left: 730px; --top: var(--red-top);  --bottom: var(--red-bottom); }
  .banner--five  { left: 949px; }

  .banner__header {
    height: 58px;
    background: linear-gradient(var(--top), var(--bottom));
    text-align: center;
    padding-top: 3px;
    border-bottom: 2px solid rgba(255,255,255,0.35);
    text-shadow: 0 1px 1px rgba(0,0,0,0.35);
  }
  .banner__title {
    display: block;
    font-size: 25px;
    line-height: 28px;
    font-weight: 400;
  }
  .banner__subtitle {
    display: block;
    font-size: 19px;
    line-height: 20px;
  }

  .banner__photo {
    position: relative;
    height: 303px;
    background: linear-gradient(90deg, var(--skin-deep) 0%, var(--skin-light) 45%, var(--white) 75%);
  }

  .photo-offer {
    position: absolute;
    right: 11px;
    bottom: 8px;
    text-align: right;
    color: var(--ink);
    line-height: 1;
  }
  .photo-offer__lead { display: block; font-size: 30px; }
  .photo-offer__line { display: block; font-size: 17px; margin-top: 2px; }

  .banner__body {
    height: 239px;
    background: linear-gradient(var(--top), var(--bottom));
    text-align: center;
    padding-top: 6px;
  }
  .headline__intro {
    display: block;
    font-size: 34px;
    line-height: 34px;
  }
  .headline__key {
    display: block;
    font-size: 37px;
    line-height: 40px;
    letter-spacing: 0.5px;
  }
  .headline__question {
    display: block;
    font-size: 20px;
    line-height: 20px;
    font-weight: 700;
  }

  .tagline {
    display: block;
    margin-top: 21px;
    font-size: 21px;
    color: var(--ink);
  }

  .offer {
    display: block;
    margin-top: 14px;
    color: var(--red-ink);
    line-height: 1;
  }
  .offer__lead { display: block; font-size: 20px; font-weight: 700; }
  .offer__line { display: block; font-size: 12px; margin-top: 1px; }

  .cta {
    display: block;
    width: 146px;
    height: 34px;
    margin: 16px auto 0;
    border-radius: 5px;
    border: 1px solid rgba(0,0,0,0.45);
    background: linear-gradient(var(--btn-top) 0%, var(--btn-top) 48%, var(--btn-bottom) 52%, var(--btn-bottom) 100%);
    box-shadow: 1px 3px 3px rgba(0,0,0,0.5);
    font-family: "Oswald", "Arial Narrow", sans-serif;
    font-weight: 600;
    font-size: 18px;
    line-height: 32px;
    color: var(--white);
    text-shadow: 0 1px 1px rgba(0,0,0,0.5);
    text-decoration: none;
    --btn-top: var(--btn-red-top);
    --btn-bottom: var(--btn-red-bottom);
  }
  .cta--green { --btn-top: var(--btn-green-top); --btn-bottom: var(--btn-green-bottom); }
  .cta--blue  { --btn-top: var(--btn-blue-top);  --btn-bottom: var(--btn-blue-bottom); margin-top: 14px; }

  .banner--four .tagline--below {
    margin-top: 12px;
    font-size: 17px;
    color: var(--white);
  }
  .banner--four .banner__body { padding-top: 8px; }
</style>
</head>
<body>
<main class="canvas">

  <section class="banner banner--one">
    <header class="banner__header">
      <span class="banner__title">Professional</span>
      <span class="banner__subtitle">Resume Writers</span>
    </header>
    <div class="banner__photo" role="img" aria-label="Photo of a woman's face built from scattered jigsaw pieces"></div>
    <div class="banner__body">
      <h2 class="headline">
        <span class="headline__intro">Is your</span>
        <span class="headline__key">RESUME</span>
        <span class="headline__question">good enough?</span>
      </h2>
      <span class="tagline">Ask the Experts!</span>
      <a class="cta" href="#">CLICK HERE</a>
    </div>
  </section>

  <section class="banner banner--two">
    <header class="banner__header">
      <span class="banner__title">Professional</span>
      <span class="banner__subtitle">Resume Writers</span>
    </header>
    <div class="banner__photo" role="img" aria-label="Photo of a woman's face built from scattered jigsaw pieces"></div>
    <div class="banner__body">
      <h2 class="headline">
        <span class="headline__intro">Is your</span>
        <span class="headline__key">RESUME</span>
        <span class="headline__question">good enough?</span>
      </h2>
      <span class="tagline">Ask the Experts!</span>
      <a class="cta cta--green" href="#">CLICK HERE</a>
    </div>
  </section>

  <section class="banner banner--three">
    <header class="banner__header">
      <span class="banner__title">Professional</span>
      <span class="banner__subtitle">Resume Writers</span>
    </header>
    <div class="banner__photo" role="img" aria-label="Photo of a woman's face built from scattered jigsaw pieces"></div>
    <div class="banner__body">
      <h2 class="headline">
        <span class="headline__intro">Is your</span>
        <span class="headline__key">RESUME</span>
        <span class="headline__question">good enough?</span>
      </h2>
      <span class="tagline">Ask the Experts!</span>
      <a class="cta" href="#">CLICK HERE</a>
    </div>
  </section>

  <section class="banner banner--four">
    <header class="banner__header">
      <span class="banner__title">Professional</span>
      <span class="banner__subtitle">Resume Writers</span>
    </header>
    <div class="banner__photo" role="img" aria-label="Photo of a woman's face built from scattered jigsaw pieces"></div>
    <div class="banner__body">
      <h2 class="headline">
        <span class="headline__intro">Is your</span>
        <span class="headline__key">RESUME</span>
        <span class="headline__question">good enough?</span>
      </h2>
      <span class="offer">
        <span class="offer__lead">FREE RESUME</span>
        <span class="offer__line">HEALTH CHECK</span>
      </span>
      <a class="cta cta--blue" href="#">CLICK HERE</a>
      <span class="tagline tagline--below">Ask the Experts!</span>
    </div>
  </section>

  <section class="banner banner--five">
    <header class="banner__header">
      <span class="banner__title">Professional</span>
      <span class="banner__subtitle">Resume Writers</span>
    </header>
    <div class="banner__photo" role="img" aria-label="Photo of a woman's face built from scattered jigsaw pieces">
      <p class="photo-offer">
        <span class="photo-offer__lead">FREE</span>
        <span class="photo-offer__line">RESUME</span>
        <span class="photo-offer__line">HEALTH CHECK</span>
      </p>
    </div>
    <div class="banner__body">
      <h2 class="headline">
        <span class="headline__intro">Is your</span>
        <span class="headline__key">RESUME</span>
        <span class="headline__question">good enough?</span>
      </h2>
      <span class="tagline">Ask the Experts!</span>
      <a class="cta" href="#">CLICK HERE</a>
    </div>
  </section>

</main>
</body>
</html>
```